VELINTA Promotions - Business Card Design Project

We are looking for a classy business cards for Promotion Company based in Toronto, Canada named Velinta Promotions.

Velinta Promotions has an idea and vision to set high standard, be EXCLUSIVE and attract a group of people that will follow us through events we promote (night clubs, brand promotions, music events, and sport events)

We want to present a high standards and classy image to the others...
Updates

Target Market(s)

male/female age 25-40 Target: business owners young entrepreneur - clubing industry - media industry - promotion industry - marketing media industry

Industry/Entity Type

Events

Requirements
Must have
• business cards should be classy, make people feel exclusive , make people react ..

```html
<!DOCTYPE html>
<html lang="en">
<head>
<meta charset="utf-8">
<title>Velinta Promotions – Business Card</title>
<link rel="stylesheet" href="https://fonts.googleapis.com/css2?family=Arimo:wght@700&family=Cinzel:wght@400&display=swap">
<style>
  :root {
    --page: #ffffff;
    --card: #161616;
    --sheen-top: #363636;
    --sheen-bottom: #1c1c1c;
    --cyan: #3fd3dd;
    --cloud-grey: #5c5c5c;
    --cloud-cyan: #2b8e95;
    --rule: #6a6a6a;
    --white: #ffffff;
  }
  * { box-sizing: border-box; margin: 0; padding: 0; }
  html, body { width: 765px; height: 1200px; overflow: hidden; background: var(--page); }
  .sheet { position: relative; width: 765px; height: 1200px; }

  .panel { position: absolute; left: 18px; width: 729px; background: var(--card); overflow: hidden; }
  .panel--back { top: 18px; height: 437px; }
  .panel--spread { top: 479px; height: 237px; }
  .panel--front { top: 743px; height: 437px; }

  .card { position: absolute; left: 0; top: 0; width: 729px; height: 437px; overflow: hidden; }
  .card--mini { transform: scale(0.5); transform-origin: 0 0; top: 9px; }
  .card--mini.left { left: 0; }
  .card--mini.right { left: 364.5px; }

  .sheen { position: absolute; inset: 0; width: 100%; height: 100%; }

  .word-cloud {
    position: absolute; left: 62px; top: 58px; width: 250px; height: 300px;
    background: linear-gradient(160deg, var(--cloud-grey), var(--cloud-cyan));
    opacity: .55; border-radius: 4px;
  }

  .divider { position: absolute; left: 321px; top: 90px; width: 1px; height: 310px; background: var(--rule); }

  .brand { position: absolute; display: flex; align-items: center; gap: 10px; color: var(--cyan);
    font-family: "Cinzel", serif; font-weight: 400; }
  .brand-mark { border: 2px solid var(--cyan); flex: none; }
  .brand-name { display: flex; flex-direction: column; align-items: center; line-height: 1; }
  .brand--small { left: 339px; top: 108px; }
  .brand--small .brand-mark { width: 30px; height: 30px; }
  .brand--small .name { font-size: 46px; letter-spacing: 1px; }
  .brand--small .tag { font-size: 11px; letter-spacing: 5px; margin-top: 4px; }
  .brand--large { left: 0; right: 0; top: 180px; justify-content: center; }
  .brand--large .brand-mark { width: 52px; height: 52px; }
  .brand--large .name { font-size: 88px; letter-spacing: 2px; }
  .brand--large .tag { font-size: 19px; letter-spacing: 10px; margin-top: 6px; }

  .contacts { position: absolute; left: 352px; top: 194px; list-style: none;
    font-family: "Arimo", sans-serif; font-weight: 700; font-size: 12px; color: var(--white); }
  .contacts li { display: flex; align-items: center; gap: 12px; height: 29px; }
  .contacts svg { width: 16px; height: 16px; flex: none; }
  .contacts .square { width: 15px; height: 15px; background: var(--cyan); border-radius: 2px; flex: none; }
</style>
</head>
<body>
<main class="sheet">

  <svg width="0" height="0" style="position:absolute">
    <defs>
      <linearGradient id="sheenFill" x1="0" y1="0" x2="0" y2="1">
        <stop offset="0" stop-color="#363636"/><stop offset="1" stop-color="#1c1c1c"/>
      </linearGradient>
    </defs>
  </svg>

  <!-- Back side -->
  <section class="panel panel--back">
    <div class="card">
      <svg class="sheen" viewBox="0 0 729 437" preserveAspectRatio="none">
        <path d="M0 437 C150 300 250 70 420 35 C560 10 680 55 729 85 L729 437 Z" fill="url(#sheenFill)"/>
      </svg>
      <div class="word-cloud" role="img" aria-label="Typographic word cloud of event services: night clubs, brand promotions, music events, sports events"></div>
      <div class="divider"></div>
      <div class="brand brand--small">
        <span class="brand-mark"></span>
        <span class="brand-name"><span class="name">VELINTA</span><span class="tag">PROMOTIONS</span></span>
      </div>
      <ul class="contacts">
        <li><svg viewBox="0 0 16 16"><path fill="var(--cyan)" d="M3 2h3l1 4-2 1c1 2 2 3 4 4l1-2 4 1v3c0 1-1 1-2 1C6 14 2 10 2 4c0-1 0-2 1-2z"/></svg>+1.416.555.0192</li>
        <li><svg viewBox="0 0 16 16"><rect x="1" y="3" width="14" height="10" fill="var(--cyan)"/><path d="M1 3l7 6 7-6" fill="none" stroke="var(--card)" stroke-width="1.5"/></svg>HELLO@VELINTAPROMO.CA</li>
        <li><svg viewBox="0 0 16 16"><path fill="var(--cyan)" d="M8 1a5 5 0 0 1 5 5c0 4-5 9-5 9S3 10 3 6a5 5 0 0 1 5-5z"/><circle cx="8" cy="6" r="2" fill="var(--card)"/></svg>P.O. BOX 4417, TORONTO, ONTARIO</li>
        <li><span class="square"></span>WWW.VELINTAPROMO.CA/EVENTS</li>
        <li><span class="square"></span>WWW.VELINTAPROMO.CA/NEWS</li>
      </ul>
    </div>
  </section>

  <!-- Open spread -->
  <section class="panel panel--spread">
    <div class="card card--mini left">
      <svg class="sheen" viewBox="0 0 729 437" preserveAspectRatio="none">
        <path d="M0 437 C150 300 250 70 420 35 C560 10 680 55 729 85 L729 437 Z" fill="url(#sheenFill)"/>
      </svg>
      <div class="word-cloud" role="img" aria-label="Typographic word cloud of event services"></div>
      <div class="divider"></div>
      <div class="brand brand--small">
        <span class="brand-mark"></span>
        <span class="brand-name"><span class="name">VELINTA</span><span class="tag">PROMOTIONS</span></span>
      </div>
      <ul class="contacts">
        <li><svg viewBox="0 0 16 16"><path fill="var(--cyan)" d="M3 2h3l1 4-2 1c1 2 2 3 4 4l1-2 4 1v3c0 1-1 1-2 1C6 14 2 10 2 4c0-1 0-2 1-2z"/></svg>+1.416.555.0192</li>
        <li><svg viewBox="0 0 16 16"><rect x="1" y="3" width="14" height="10" fill="var(--cyan)"/><path d="M1 3l7 6 7-6" fill="none" stroke="var(--card)" stroke-width="1.5"/></svg>HELLO@VELINTAPROMO.CA</li>
        <li><svg viewBox="0 0 16 16"><path fill="var(--cyan)" d="M8 1a5 5 0 0 1 5 5c0 4-5 9-5 9S3 10 3 6a5 5 0 0 1 5-5z"/><circle cx="8" cy="6" r="2" fill="var(--card)"/></svg>P.O. BOX 4417, TORONTO, ONTARIO</li>
        <li><span class="square"></span>WWW.VELINTAPROMO.CA/EVENTS</li>
        <li><span class="square"></span>WWW.VELINTAPROMO.CA/NEWS</li>
      </ul>
    </div>
    <div class="card card--mini right">
      <svg class="sheen" viewBox="0 0 729 437" preserveAspectRatio="none">
        <path d="M0 437 C150 300 250 70 420 35 C560 10 680 55 729 85 L729 437 Z" fill="url(#sheenFill)"/>
      </svg>
      <div class="brand brand--large">
        <span class="brand-mark"></span>
        <span class="brand-name"><span class="name">VELINTA</span><span class="tag">PROMOTIONS</span></span>
      </div>
    </div>
  </section>

  <!-- Front side -->
  <section class="panel panel--front">
    <div class="card">
      <svg class="sheen" viewBox="0 0 729 437" preserveAspectRatio="none">
        <path d="M0 437 C150 300 250 70 420 35 C560 10 680 55 729 85 L729 437 Z" fill="url(#sheenFill)"/>
      </svg>
      <div class="brand brand--large">
        <span class="brand-mark"></span>
        <span class="brand-name"><span class="name">VELINTA</span><span class="tag">PROMOTIONS</span></span>
      </div>
    </div>
  </section>

</main>
</body>
</html>
```